Design a web site for my business - Brellan Coatworks Mackaby.

We are a family business that handles design, fabrication and installation of powder coated aluminum, stainless steel and glass products. Including handrails, privacy slat screens, electric gates and pool fencing. We are based in the Whitsundays in North Queensland and service an area from Airlie Beach to Townsville.

Target Market(s)

Domestic and commercial

Industry/Entity Type

fabrication - manufacturing

Coding

Coded - Design and coding required

Number of Pages Required

5+ page

Colors
0054AA
0677BA
7BADD7
CADEEF
E8F1F8

Requirements
Must have
• photo galleries, contact page, one page for privacy screens, balustrades, glass fencing, stainless steel handrail, powder coated aluminium handrails and pool fencing

```html
<!DOCTYPE html>
<html lang="en">
<head>
<meta charset="utf-8">
<title>Brellan Coatworks Mackaby — Aluminium, Stainless Steel &amp; Glass</title>
<link href="https://fonts.googleapis.com/css2?family=Montserrat:wght@400;500;600;700;800&display=swap" rel="stylesheet">
<style>
:root{
  --navy:#1b2a4b;
  --navy-deep:#16233f;
  --cyan:#12cfe0;
  --cyan-dark:#0fb3c6;
  --blue:#0054aa;
  --blue-mid:#0677ba;
  --blue-soft:#7badd7;
  --blue-pale:#cadeef;
  --blue-wash:#f3f7fc;
  --ink:#1b2a4b;
  --white:#ffffff;
  --star:#f5b400;
}
*{box-sizing:border-box;margin:0;padding:0}
html,body{width:1200px;height:3333px;overflow:hidden}
body{font-family:'Montserrat',sans-serif;color:var(--ink);background:var(--white);position:relative}
.section{position:absolute;left:0;width:1200px}
.btn{display:inline-block;font-family:'Montserrat',sans-serif;font-weight:600;text-transform:uppercase;font-size:11px;letter-spacing:.3px;padding:9px 16px;border-radius:3px;text-decoration:none}
.btn-cyan{background:var(--cyan);color:var(--navy)}
.btn-outline-light{border:1.5px solid var(--white);color:var(--white)}
.btn-outline-dark{border:1.5px solid var(--navy);color:var(--navy);background:var(--white)}

/* hero */
.hero{top:0;height:447px;overflow:hidden}
.hero-photo{position:absolute;inset:0;background:
  radial-gradient(ellipse at 75% 40%,rgba(214,160,90,.85) 0,rgba(214,160,90,0) 35%),
  linear-gradient(180deg,rgba(0,0,0,0) 70%,rgba(48,112,40,.9) 100%),
  linear-gradient(90deg,#1d3566 0%,#1e4ea8 45%,#2f7df2 100%)}
.hero-shade{position:absolute;inset:0;background:linear-gradient(90deg,rgba(20,35,70,.75) 0%,rgba(20,35,70,.25) 55%,rgba(0,0,0,0) 100%)}
.nav{position:absolute;top:22px;left:118px;right:116px;display:flex;align-items:center}
.brand{display:flex;align-items:center;gap:8px;color:var(--white);font-weight:800;font-size:18px;letter-spacing:.2px;text-decoration:none}
.brand-dot{width:10px;height:10px;border-radius:50%;background:var(--cyan)}
.nav-links{margin-left:auto;display:flex;gap:16px;align-items:center;list-style:none}
.nav-links a{color:var(--white);font-size:10px;font-weight:500;text-decoration:none;letter-spacing:.4px}
.nav-links .btn{padding:6px 14px;font-size:10px;margin-left:4px;color:var(--navy)}
.hero-copy{position:absolute;left:116px;top:130px;width:440px;color:var(--white)}
.hero-copy h1{font-size:33px;font-weight:700;line-height:1.12;letter-spacing:.3px}
.hero-copy p{font-size:11px;line-height:1.45;margin-top:20px;width:420px}
.hero-actions{display:flex;gap:14px;margin-top:22px}
.hero-actions .btn{font-size:10px;padding:7px 14px}

/* stats */
.stats{top:447px;height:143px;background:var(--blue-wash);text-align:center}
.stats h2{font-size:19px;font-weight:600;margin-top:22px;letter-spacing:.2px}
.stat-row{display:flex;justify-content:center;margin-top:22px}
.stat{display:flex;align-items:center;gap:12px;padding:0 22px;height:44px;border-left:1.5px solid var(--blue-soft)}
.stat:first-child{border-left:none}
.stat-num{font-size:30px;font-weight:700;color:var(--cyan)}
.stat-num.small{font-size:24px}
.stat-label{font-size:13px;text-align:left;line-height:1.05;color:var(--ink)}

/* intro */
.intro{top:590px;height:515px;overflow:hidden}
.tri{position:absolute}
.intro-title{text-align:center;font-size:29px;font-weight:600;margin-top:46px;letter-spacing:.3px}
.intro-lead{text-align:center;font-size:19px;line-height:1.2;width:760px;margin:22px auto 0;font-weight:400}
.photo{position:absolute}
.intro-photo-a{left:137px;top:217px;width:225px;height:228px;background:linear-gradient(180deg,#7fd0ef 0%,#d9e7e6 45%,#37c7dc 70%,#11b7cf 100%)}
.intro-photo-b{left:377px;top:257px;width:226px;height:228px;background:linear-gradient(180deg,#e9f4fb 0%,#4fb2e6 45%,#1888c9 65%,#c9d4dc 100%)}
.intro-text{position:absolute;left:659px;top:238px;width:395px}
.intro-text h3{font-size:22px;font-weight:600;line-height:1.15}
.intro-text p{font-size:13px;line-height:1.22;margin-top:20px;color:var(--ink)}
.intro-text .btn{margin-top:24px;font-size:10px;padding:8px 24px;margin-left:-4px}

/* services */
.services{top:1105px;height:420px;text-align:center}
.big-title{font-size:41px;font-weight:800;letter-spacing:1px}
.services .big-title{margin-top:22px}
.services-sub{font-size:14px;margin-top:14px;color:var(--ink)}
.service-grid{display:flex;gap:17px;justify-content:center;margin-top:28px}
.service-card{position:relative;width:272px;height:262px;overflow:hidden;text-align:left}
.service-card .photo{inset:0}
.service-card::after{content:"";position:absolute;inset:0;background:linear-gradient(180deg,rgba(22,35,63,0) 35%,rgba(22,35,63,.92) 75%)}
.service-info{position:absolute;left:17px;bottom:20px;right:36px;z-index:1;color:var(--white)}
.service-info h3{font-size:20px;font-weight:700;letter-spacing:.3px}
.service-info p{font-size:11.5px;line-height:1.15;margin-top:12px}
.service-info a{display:inline-block;font-size:8.5px;font-weight:700;color:var(--cyan);margin-top:10px;text-decoration:underline}
.ph-handrails{background:linear-gradient(180deg,#c9c2b6 0%,#8d8577 40%,#40424a 100%)}
.ph-screens{background:linear-gradient(180deg,#ddd8cf 0%,#8b857c 40%,#2f3034 100%)}
.ph-gates{background:linear-gradient(180deg,#6f8a5a 0%,#9a9a94 35%,#2e3338 100%)}
.ph-pool{background:linear-gradient(180deg,#7fa27c 0%,#4e7d5a 40%,#3d8fb2 80%)}

/* process */
.process{top:1525px;height:370px;text-align:center}
.process .big-title{font-size:30px;margin-top:14px}
.steps{display:flex;justify-content:center;margin-top:42px;margin-left:-6px}
.step{position:relative;width:255px;height:124px}
.step-icon{position:absolute;left:50%;top:8px;transform:translateX(-50%);margin-left:-20px}
.step-num{position:absolute;top:2px;right:48px;font-size:34px;font-weight:600;color:var(--cyan)}
.step-label{position:absolute;left:0;right:40px;top:80px;font-size:15px;font-weight:600}
.step-divider{position:absolute;right:0;top:0}
.process .btn{margin-top:28px;font-size:12px;padding:9px 18px;font-weight:500}

/* materials */
.materials{top:1863px;height:277px;text-align:center}
.ghost{position:absolute;left:0;right:0;top:6px;font-size:55px;font-weight:800;color:var(--blue-wash);letter-spacing:2px}
.materials h2{position:relative;font-size:24px;font-weight:800;letter-spacing:.5px;margin-top:20px}
.material-grid{display:flex;gap:18px;justify-content:center;margin-top:34px}
.material-card{position:relative;width:311px;height:172px;overflow:hidden;text-align:left}
.material-card .photo{inset:0}
.material-card::after{content:"";position:absolute;inset:0;background:linear-gradient(180deg,rgba(22,35,63,0) 30%,rgba(22,35,63,.7) 100%)}
.material-info{position:absolute;left:18px;bottom:14px;width:190px;z-index:1;color:var(--white)}
.material-info h3{font-size:18px;font-weight:700;line-height:1.05}
.material-info p{font-size:11.5px;line-height:1.05;margin-top:10px}
.ph-aluminium{background:repeating-linear-gradient(90deg,#2b3445 0 6px,#4b5468 6px 9px)}
.ph-steel{background:linear-gradient(135deg,#e9eaec 0%,#9c9fa5 40%,#545860 100%)}
.ph-glass{background:linear-gradient(160deg,#7fb3e6 0%,#3c5f8f 45%,#253b5c 100%)}

/* service area */
.area{top:2140px;height:317px;background:var(--blue-wash)}
.area-copy{position:absolute;left:167px;top:62px;width:380px}
.area-copy h2{font-size:23px;font-weight:700;letter-spacing:.5px}
.area-copy p{font-size:11px;line-height:1.4;margin-top:14px}
.area-list{display:grid;grid-template-columns:103px 95px 150px;row-gap:12px;margin-top:18px;font-size:16px;font-weight:500;letter-spacing:.4px}
.area-copy .btn{margin-top:26px;font-size:11px;padding:9px 28px;font-weight:500}
.area-map{position:absolute;left:604px;top:14px;width:394px;height:282px;border-radius:6px;background:linear-gradient(180deg,#10c4d6 0%,#0b8fa6 50%,#16334e 100%)}

/* testimonials */
.testimonials{top:2457px;height:336px}
.eyebrow{position:absolute;left:157px;top:46px;font-size:12px;color:var(--cyan-dark);letter-spacing:.4px}
.testimonials h2{position:absolute;left:156px;top:70px;width:780px;font-size:26px;font-weight:600;line-height:1.1;letter-spacing:.3px}
.view-all{position:absolute;right:159px;top:78px;font-size:9.5px;color:var(--cyan-dark);text-decoration:none}
.quote-grid{position:absolute;left:156px;top:152px;display:flex;gap:15px}
.quote{width:291px;height:150px;border:1.5px solid var(--navy);padding:12px 22px 0}
.stars{color:var(--star);font-size:10px;letter-spacing:2px}
.quote p{font-size:11px;line-height:1.25;margin-top:6px;height:58px}
.quote-rule{height:2px;background:var(--cyan);margin:0 0 10px}
.author{display:flex;align-items:center;gap:8px}
.avatar{width:20px;height:20px;border-radius:50%;background:var(--cyan);color:var(--white);font-size:11px;font-weight:700;display:flex;align-items:center;justify-content:center}
.author b{display:block;font-size:10px}
.author span{font-size:9px}

/* call to action */
.cta{top:2799px;height:302px;overflow:hidden}
.cta-photo{position:absolute;inset:0;background:
  linear-gradient(180deg,rgba(0,0,0,0) 72%,rgba(32,50,38,.9) 100%),
  linear-gradient(90deg,#e2ddd3 0%,#cdd4da 45%,#a9bfd4 100%)}
.blob{position:absolute;border-radius:50%;background:var(--cyan)}
.cta-copy{position:absolute;left:667px;top:75px;width:360px}
.cta-copy h2{font-size:26px;font-weight:700;line-height:1.07;letter-spacing:.3px}
.cta-copy p{font-size:12px;line-height:1.2;margin-top:14px}
.cta-copy .btn{margin-top:14px;font-size:11px;padding:7px 14px}

/* footer */
.footer{top:3101px;height:232px;background:var(--navy);color:var(--white);overflow:hidden}
.footer-brand{position:absolute;left:134px;top:54px}
.footer-brand .brand{font-size:22px}
.footer-tag{font-size:7px;letter-spacing:1px;margin-top:4px;margin-left:20px}
.socials{display:flex;gap:5px;margin-top:14px;margin-left:10px}
.social{width:26px;height:26px;border-radius:50%;border:1.5px solid var(--white)}
.footer-col{position:absolute;top:26px}
.footer-col h4{font-size:10px;font-weight:600;letter-spacing:.5px;margin-bottom:14px}
.footer-col ul{list-style:none}
.footer-col li{font-size:9.5px;line-height:1.45}
.col-nav{left:448px}
.col-services{left:587px}
.col-contact{left:808px}
.contact-row{display:flex;align-items:center;gap:12px;margin-left:-1px;margin-bottom:10px}
.contact-row svg{flex:none}
.contact-row span{font-size:10px;line-height:1.35}
.contact-row .phone{font-size:15px;font-weight:500}
.copyright{position:absolute;left:0;right:0;bottom:22px;text-align:center;font-size:9.5px}
</style>
</head>
<body>

<section class="section hero">
  <div class="hero-photo" role="img" aria-label="Modern two-storey timber-clad home with glass balustrade balcony at dusk"></div>
  <div class="hero-shade"></div>
  <nav class="nav">
    <a class="brand" href="#"><span class="brand-dot"></span>BRELLAN COATWORKS</a>
    <ul class="nav-links">
      <li><a href="#">ABOUT</a></li>
      <li><a href="#">SERVICES</a></li>
      <li><a href="#">PROJECTS</a></li>
      <li><a href="#">SERVICE AREAS</a></li>
      <li><a href="#">TESTIMONIALS</a></li>
      <li><a href="#">CONTACT</a></li>
      <li><a class="btn btn-cyan" href="#">GET FREE QUOTE</a></li>
    </ul>
  </nav>
  <div class="hero-copy">
    <h1>Premium Aluminium, Stainless Steel &amp; Glass Solutions.</h1>
    <p>Family-owned specialists delivering custom-designed handrails, privacy screens, electric gates and pool fencing across the Whitsundays and North Queensland.</p>
    <div class="hero-actions">
      <a class="btn btn-cyan" href="#">Request Free Quote</a>
      <a class="btn btn-outline-light" href="#">View Our Projects</a>
    </div>
  </div>
</section>

<section class="section stats">
  <h2>Why Homeowners &amp; Builders Choose Us</h2>
  <div class="stat-row">
    <div class="stat"><span class="stat-num">20+</span><span class="stat-label">Years<br>Experience</span></div>
    <div class="stat" style="padding-left:60px"><span class="stat-num small">500+</span><span class="stat-label">Projects<br>Completed</span></div>
    <div class="stat"><span class="stat-num small">9,765,411</span><span class="stat-label">Australian<br>Made</span></div>
    <div class="stat"><span class="stat-num small">100%</span><span class="stat-label">Customer<br>Satisfaction</span></div>
  </div>
</section>

<section class="section intro">
  <svg class="tri" style="left:0;top:78px" width="101" height="160" viewBox="0 0 101 160"><polygon points="0,0 101,62 0,160" fill="#12cfe0"/></svg>
  <svg class="tri" style="right:0;top:260px" width="72" height="115" viewBox="0 0 72 115"><polygon points="72,0 0,70 72,115" fill="#12cfe0"/></svg>
  <h2 class="intro-title">Crafted with Precision. Built on Family Values.</h2>
  <p class="intro-lead">As a proud family-owned business based in the Whitsundays, we specialise in the design, fabrication, and installation of premium aluminium, stainless steel, and glass solutions.</p>
  <div class="photo intro-photo-a" role="img" aria-label="Aluminium slat pool fence beside a turquoise swimming pool"></div>
  <div class="photo intro-photo-b" role="img" aria-label="Frameless glass balustrade on a deck overlooking the ocean"></div>
  <div class="intro-text">
    <h3>Crafted with Precision. Built on Family Values.</h3>
    <p>Every project is custom-made to suit your property, combining quality craftsmanship with durable materials and attention to detail.</p>
    <p>From modern handrails and privacy screens to electric gates and pool fencing, we work closely with homeowners, builders, and commercial clients to deliver functional, stylish, and long-lasting results.</p>
    <a class="btn btn-outline-dark" href="#">Read More</a>
  </div>
</section>

<section class="section services">
  <h2 class="big-title">OUR SERVICES</h2>
  <p class="services-sub">Every product is designed and fabricated to suit your unique space and requirements</p>
  <div class="service-grid">
    <article class="service-card">
      <div class="photo ph-handrails" role="img" aria-label="Grand staircase with stainless steel handrails"></div>
      <div class="service-info"><h3>Handrails</h3><p>Safe, stylish aluminium and stainless steel handrails.</p><a href="#">+ READ MORE</a></div>
    </article>
    <article class="service-card">
      <div class="photo ph-screens" role="img" aria-label="Dark aluminium slat privacy screen in a modern interior"></div>
      <div class="service-info"><h3>Privacy Screens</h3><p>Enhance privacy while improving modern street appeal.</p><a href="#">+ READ MORE</a></div>
    </article>
    <article class="service-card">
      <div class="photo ph-gates" role="img" aria-label="Dark slatted electric driveway gates between stone pillars"></div>
      <div class="service-info"><h3>Electric Gates</h3><p>Custom automated gates designed for security and convenience.</p><a href="#">+ READ MORE</a></div>
    </article>
    <article class="service-card">
      <div class="photo ph-pool" role="img" aria-label="Garden pool with pergola and fencing"></div>
      <div class="service-info"><h3>Pool Fencing</h3><p>Safe, stylish aluminium and stainless steel handrails.</p><a href="#">+ READ MORE</a></div>
    </article>
  </div>
</section>

<section class="section process">
  <h2 class="big-title">OUR PROCESS</h2>
  <div class="steps">
    <div class="step">
      <svg class="step-icon" width="72" height="56" viewBox="0 0 72 56" fill="none" stroke="#12cfe0" stroke-width="2"><circle cx="12" cy="10" r="6"/><circle cx="60" cy="10" r="6"/><rect x="24" y="2" width="24" height="16" rx="2"/><path d="M4 54V28q0-8 8-8t8 8v26M52 54V28q0-8 8-8t8 8v26M20 34h32M30 34v20M42 34v20"/></svg>
      <span class="step-num">1</span><span class="step-label">Consultation</span>
      <svg class="step-divider" width="26" height="124" viewBox="0 0 26 124" fill="none" stroke="#1b2a4b" stroke-width="1.5"><path d="M2 0V50L22 62L2 74V124"/></svg>
    </div>
    <div class="step">
      <svg class="step-icon" width="80" height="56" viewBox="0 0 80 56" fill="none" stroke="#12cfe0" stroke-width="2"><path d="M6 50a34 34 0 0 1 68 0z"/><path d="M40 50L28 34"/><rect x="18" y="14" width="7" height="20"/><rect x="29" y="6" width="7" height="24"/><rect x="40" y="2" width="7" height="26"/><rect x="51" y="8" width="7" height="22"/></svg>
      <span class="step-num">2</span><span class="step-label">Measure &amp; Quote</span>
      <svg class="step-divider" width="26" height="124" viewBox="0 0 26 124" fill="none" stroke="#1b2a4b" stroke-width="1.5"><path d="M2 0V50L22 62L2 74V124"/></svg>
    </div>
    <div class="step">
      <svg class="step-icon" width="74" height="56" viewBox="0 0 74 56" fill="none" stroke="#12cfe0" stroke-width="2"><rect x="2" y="2" width="60" height="46" rx="4"/><path d="M2 14h60M10 24h24M10 34h18"/><circle cx="42" cy="24" r="3"/><circle cx="34" cy="34" r="3"/><path d="M52 30l16 16-7 1 4 8-4 2-4-8-5 4z"/></svg>
      <span class="step-num">3</span><span class="step-label">Custom Design</span>
      <svg class="step-divider" width="26" height="124" viewBox="0 0 26 124" fill="none" stroke="#1b2a4b" stroke-width="1.5"><path d="M2 0V50L22 62L2 74V124"/></svg>
    </div>
    <div class="step">
      <svg class="step-icon" width="72" height="56" viewBox="0 0 72 56" fill="none" stroke="#12cfe0" stroke-width="2"><circle cx="40" cy="22" r="18"/><circle cx="40" cy="22" r="8"/><path d="M27 35L6 52M14 30l-8 6M62 8l4-4"/></svg>
      <span class="step-num">1</span><span class="step-label">Final Inspection</span>
      <svg class="step-divider" width="26" height="124" viewBox="0 0 26 124" fill="none" stroke="#1b2a4b" stroke-width="1.5"><path d="M2 0V50L22 62L2 74V124"/></svg>
    </div>
  </div>
  <a class="btn btn-outline-dark" href="#">Request Free Quote</a>
</section>

<section class="section materials">
  <div class="ghost" aria-hidden="true">MATERIALS WE USE</div>
  <h2>MATERIALS WE USE</h2>
  <div class="material-grid">
    <article class="material-card">
      <div class="photo ph-aluminium" role="img" aria-label="Close-up of dark powder coated aluminium slats"></div>
      <div class="material-info"><h3>Powder Coated Aluminium</h3><p>Lightweight, durable and corrosion-resistant.</p></div>
    </article>
    <article class="material-card">
      <div class="photo ph-steel" role="img" aria-label="Stainless steel balustrade and column in a modern building"></div>
      <div class="material-info"><h3>Stainless Steel</h3><p>Strong, modern and built to withstand harsh conditions.</p></div>
    </article>
    <article class="material-card">
      <div class="photo ph-glass" role="img" aria-label="Glass facade of a modern building against blue sky"></div>
      <div class="material-info"><h3>Architectural Glass</h3><p>Elegant safety glass for unobstructed views.</p></div>
    </article>
  </div>
</section>

<section class="section area">
  <div class="area-copy">
    <h2>SERVICE AREA MAP</h2>
    <p>As a family-owned business, we pride ourselves on delivering exceptional workmanship, honest advice and long-lasting relationships with every client.</p>
    <div class="area-list"><span>AIRLIE</span><span>BEACH</span><span>WHITSUNDAYS</span><span>BOWEN</span><span>AYR</span><span>TOWNSVILLE</span></div>
    <a class="btn btn-outline-dark" href="#">Check Your Area</a>
  </div>
  <div class="area-map" role="img" aria-label="Map of Australia with location pins marking the North Queensland service areas"></div>
</section>

<section class="section testimonials">
  <span class="eyebrow">CUSTOMER TESTIMONIALS</span>
  <h2>Trusted by Whitsunday Businesses. Proven Through Every Partnership.</h2>
  <a class="view-all" href="#">VIEW ALL</a>
  <div class="quote-grid">
    <figure class="quote">
      <div class="stars">★★★★★</div>
      <p>"Our new electric gate exceeded every expectation. Professional from start to finish."</p>
      <div class="quote-rule"></div>
      <div class="author"><span class="avatar">T</span><div><b>Talia W.</b><span>Airlie Beach</span></div></div>
    </figure>
    <figure class="quote">
      <div class="stars">★★★★★</div>
      <p>"Outstanding workmanship and attention to detail. Highly recommended."</p>
      <div class="quote-rule"></div>
      <div class="author"><span class="avatar">C</span><div><b>Corey D.</b><span>Bowen</span></div></div>
    </figure>
    <figure class="quote">
      <div class="stars">★★★★★</div>
      <p>"Beautiful frameless pool fencing installed perfectly."</p>
      <div class="quote-rule"></div>
      <div class="author"><span class="avatar">N</span><div><b>Nina P.</b><span>Townsville</span></div></div>
    </figure>
  </div>
</section>

<section class="section cta">
  <div class="cta-photo" role="img" aria-label="Contemporary white home with glass balustrades surrounded by palm trees"></div>
  <div class="blob" style="left:102px;top:93px;width:136px;height:108px"></div>
  <div class="blob" style="left:-56px;top:150px;width:184px;height:160px"></div>
  <div class="cta-copy">
    <h2>Ready to Transform Your Property?</h2>
    <p>Let's create a custom solution designed specifically for your home or business.</p>
    <a class="btn btn-cyan" href="#">Request Free Quote</a>
  </div>
</section>

<footer class="section footer">
  <div class="blob" style="left:-40px;top:-30px;width:150px;height:90px"></div>
  <div class="blob" style="left:1032px;top:95px;width:142px;height:110px"></div>
  <div class="blob" style="left:1130px;top:205px;width:120px;height:80px"></div>
  <div class="footer-brand">
    <a class="brand" href="#"><span class="brand-dot"></span>BRELLAN COATWORKS</a>
    <div class="footer-tag">FABRICATION AND INSTALLATION</div>
    <div class="socials"><span class="social"></span><span class="social"></span><span class="social"></span></div>
  </div>
  <div class="footer-col col-nav">
    <h4>NAVIGATION</h4>
    <ul><li>About</li><li>Services</li><li>Projects</li><li>Service Areas</li><li>Testimonials</li><li>Contact</li></ul>
  </div>
  <div class="footer-col col-services">
    <h4>SERVICES WE OFFER</h4>
    <ul><li>Handrails</li><li>Privacy Screens</li><li>Electric Gates</li><li>Pool Fencing</li></ul>
  </div>
  <div class="footer-col col-contact">
    <h4>CONTACT US</h4>
    <div class="contact-row">
      <svg width="26" height="26" viewBox="0 0 26 26" fill="none" stroke="#fff" stroke-width="1.5"><circle cx="13" cy="13" r="12"/><rect x="7" y="9" width="12" height="8" fill="#fff" stroke="none"/><path d="M7 9l6 5 6-5" stroke="#1b2a4b"/></svg>
      <span style="text-decoration:underline">hello@brellancoatworks.example</span>
    </div>
    <div class="contact-row">
      <svg width="26" height="26" viewBox="0 0 26 26" fill="none" stroke="#fff" stroke-width="1.5"><circle cx="13" cy="13" r="12"/><path d="M9 8c0 5 4 9 9 9l1-2-3-2-1 1c-2-1-3-2-4-4l1-1-2-3z" fill="#fff"/></svg>
      <span class="phone">07 4900 2718</span>
    </div>
    <div class="contact-row">
      <svg width="26" height="26" viewBox="0 0 26 26" fill="none" stroke="#fff" stroke-width="1.5"><circle cx="13" cy="13" r="12"/><path d="M13 20s-5-5-5-9a5 5 0 0 1 10 0c0 4-5 9-5 9z" fill="#fff"/><circle cx="13" cy="11" r="1.8" fill="#1b2a4b" stroke="none"/></svg>
      <span>14 Harbour Lane<br>Mackaby QLD 4800</span>
    </div>
  </div>
  <p class="copyright">© 2026 Brellan Coatworks Mackaby. All Rights Reserved.</p>
</footer>

</body>
</html>
```